Wageline Associates Business Card Design

We need a business card designed around our new logo. The business card should be modern in design & should communicate success, confidence, power, sophistication. The target market is young business professionals. This is for a human resource & payroll outsourcing business.

```html
<!DOCTYPE html>
<html lang="en">
<head>
<meta charset="utf-8">
<title>Wageline Associates Business Card</title>
<link rel="stylesheet" href="https://fonts.googleapis.com/css2?family=Libre+Bodoni:wght@700&display=swap">
<style>
  :root {
    --page-bg: #e6e7e9;
    --card-bg: #ffffff;
    --brand-red: #ec2227;
    --ink: #111111;
  }
  * { margin: 0; padding: 0; box-sizing: border-box; }
  html, body {
    width: 1200px;
    height: 1200px;
    overflow: hidden;
    background: var(--page-bg);
  }
  .card {
    position: absolute;
    left: 85px;
    top: 306px;
    width: 1032px;
    height: 589px;
    background: var(--card-bg);
    overflow: hidden;
    font-family: "Libre Bodoni", "Bodoni Moda", serif;
    font-weight: 700;
    color: var(--ink);
  }
  .corner-swoosh {
    position: absolute;
    left: 0;
    top: 0;
    width: 300px;
    height: 140px;
  }
  .corner-swoosh path { fill: var(--brand-red); }
  .brand-name {
    position: absolute;
    left: 76px;
    top: 262px;
    display: flex;
    align-items: center;
    gap: 14px;
    font-size: 36px;
    letter-spacing: 0.5px;
    white-space: nowrap;
  }
  .brand-dot {
    width: 18px;
    height: 18px;
    border-radius: 50%;
    background: var(--brand-red);
  }
  .holder {
    position: absolute;
    right: 75px;
    top: 84px;
    text-align: right;
  }
  .holder-name {
    font-size: 33px;
    letter-spacing: 3px;
    color: var(--brand-red);
    line-height: 1;
  }
  .holder-role {
    margin-top: 10px;
    font-size: 24px;
    letter-spacing: 2px;
    line-height: 1;
  }
  .contact-list {
    position: absolute;
    right: 0;
    top: 346px;
    list-style: none;
  }
  .contact-row {
    display: flex;
    align-items: center;
    justify-content: flex-end;
    height: 40px;
    margin-bottom: 23px;
  }
  .contact-text {
    font-size: 23px;
    letter-spacing: 3px;
    margin-right: 20px;
  }
  .contact-icon {
    width: 34px;
    height: 34px;
    margin-right: 6px;
  }
  .contact-icon path, .contact-icon rect {
    fill: none;
    stroke: var(--ink);
    stroke-width: 1.4;
    stroke-linejoin: round;
  }
  .contact-icon text {
    font-family: Arial, sans-serif;
    font-size: 34px;
    fill: var(--ink);
  }
  .contact-tab { width: 68px; height: 40px; }
  .contact-tab path { fill: var(--brand-red); }
</style>
</head>
<body>
  <main class="card">
    <svg class="corner-swoosh" viewBox="0 0 300 140" aria-hidden="true">
      <path d="M0 0 H285 C150 10 40 70 0 134 Z"/>
    </svg>

    <div class="brand-name"><span class="brand-dot"></span>Wageline Associates</div>

    <header class="holder">
      <p class="holder-name">MAREN HOLLOWAY</p>
      <p class="holder-role">Managing director</p>
    </header>

    <ul class="contact-list">
      <li class="contact-row">
        <span class="contact-text">0000000000</span>
        <svg class="contact-icon" viewBox="0 0 34 34" aria-label="Phone">
          <path d="M8 5 L13 10 L10 14 C12 19 15 22 20 24 L24 21 L29 26 L26 30 C15 29 5 19 4 8 Z"/>
        </svg>
        <svg class="contact-tab" viewBox="0 0 68 40" aria-hidden="true">
          <path d="M0 0 H68 V40 H0 A22 22 0 0 0 0 0 Z"/>
        </svg>
      </li>
      <li class="contact-row">
        <span class="contact-text">hello@wageline.net</span>
        <svg class="contact-icon" viewBox="0 0 34 34" aria-label="Email">
          <rect x="3" y="9" width="28" height="18"/>
          <path d="M3 9 L17 20 L31 9 M3 27 L13 17 M31 27 L21 17"/>
        </svg>
        <svg class="contact-tab" viewBox="0 0 68 40" aria-hidden="true">
          <path d="M0 0 H68 V40 H0 A22 22 0 0 0 0 0 Z"/>
        </svg>
      </li>
      <li class="contact-row">
        <span class="contact-text">www.wageline.net</span>
        <svg class="contact-icon" viewBox="0 0 34 34" aria-label="Website">
          <text x="1" y="29">@</text>
        </svg>
        <svg class="contact-tab" viewBox="0 0 68 40" aria-hidden="true">
          <path d="M0 0 H68 V40 H0 A22 22 0 0 0 0 0 Z"/>
        </svg>
      </li>
    </ul>
  </main>
</body>
</html>
```